Maplecrest Counseling and Consulting, LLC

We need a business card and stationary designed for a new therapy practice for Laura Whitcombe. Laura Whitcombe is a Therapist who specializes in Therapy for children dealing with trauma and/or stress. Below are some of her thoughts:
colors can include purple, blue, turquoise and green (does NOT have to be all colors) See attached Logos
Laura Whitcombe, LMHC
Maplecrest Counseling & Counseling Inc.
4382 W. Harbor Parkway
Suite 714
Boca Raton, FL 33912
Phone: 561-730-2254
Fax: 561-730-2255
Email: laura@maplecrestcc-example.com
Website: www.maplecrestcc-example.com

```html
<!DOCTYPE html>
<html lang="en">
<head>
<meta charset="utf-8">
<title>Maplecrest Counseling – Business Card</title>
<link href="https://fonts.googleapis.com/css2?family=Lato:wght@400;700&display=swap" rel="stylesheet">
<style>
  :root {
    --backdrop: #2a2a2a;
    --card: #f7f7f7;
    --green: #6e9c10;
    --grey: #555555;
    --grey-light: #9a9a9a;
    --text: #3a3a3a;
    --white: #ffffff;
  }
  html, body {
    margin: 0;
    width: 1200px;
    height: 873px;
    overflow: hidden;
    background: var(--backdrop);
    font-family: "Lato", Arial, sans-serif;
  }
  .card {
    position: absolute;
    left: 180px;
    top: 196px;
    width: 840px;
    height: 480px;
    background: var(--card);
    box-shadow: 0 18px 40px rgba(0,0,0,.5);
    overflow: hidden;
  }
  .holder {
    position: absolute;
    left: 44px;
    top: 52px;
  }
  .holder-name {
    margin: 0;
    font-size: 25px;
    line-height: 30px;
    font-weight: 700;
    color: var(--green);
    white-space: nowrap;
  }
  .holder-title {
    color: var(--grey);
    margin-left: 10px;
  }
  .holder-company {
    margin: 4px 0 0;
    font-size: 17px;
    line-height: 20px;
    color: var(--grey);
    white-space: nowrap;
  }
  .rule-green {
    position: absolute;
    left: 0;
    top: 116px;
    width: 250px;
    height: 3px;
    background: var(--green);
  }
  .rule-grey {
    position: absolute;
    left: 250px;
    top: 110px;
    width: 150px;
    height: 2px;
    background: var(--grey-light);
  }
  .brand {
    position: absolute;
    right: 60px;
    top: 80px;
    display: flex;
    align-items: center;
    gap: 14px;
  }
  .brand-dot {
    width: 18px;
    height: 18px;
    border-radius: 50%;
    background: var(--green);
  }
  .brand-name {
    font-size: 24px;
    font-weight: 700;
    color: var(--green);
    line-height: 1.2;
    text-align: right;
  }
  .contact {
    position: absolute;
    left: 60px;
    top: 250px;
    margin: 0;
    padding: 0;
    list-style: none;
  }
  .contact li {
    display: flex;
    align-items: center;
    gap: 16px;
    height: 34px;
    font-size: 17px;
    color: var(--text);
  }
  .contact svg {
    width: 20px;
    height: 20px;
    fill: var(--green);
  }
  .bands {
    position: absolute;
    left: 0;
    top: 0;
  }
  .website {
    position: absolute;
    right: 24px;
    top: 398px;
    height: 44px;
    line-height: 44px;
    font-size: 16px;
    color: var(--white);
    letter-spacing: .3px;
    white-space: nowrap;
  }
</style>
</head>
<body>
  <div class="card">
    <svg class="bands" width="840" height="480" viewBox="0 0 840 480">
      <polygon points="535,398 840,398 840,442 510,442" fill="#555555"/>
      <polygon points="0,446 512,446 500,470 0,470" fill="#6e9c10"/>
    </svg>

    <div class="holder">
      <p class="holder-name">Laura Whitcombe<span class="holder-title">LMHC</span></p>
      <p class="holder-company">Maplecrest Counseling &amp; Counseling Inc</p>
    </div>
    <div class="rule-green"></div>
    <div class="rule-grey"></div>

    <div class="brand">
      <div class="brand-dot"></div>
      <div class="brand-name">Maplecrest<br>Counseling and Consulting, Inc.</div>
    </div>

    <ul class="contact">
      <li>
        <svg viewBox="0 0 24 24"><path d="M6.6 10.8a15 15 0 0 0 6.6 6.6l2.2-2.2c.3-.3.7-.4 1-.2 1.1.4 2.3.6 3.6.6.6 0 1 .4 1 1V20c0 .6-.4 1-1 1A17 17 0 0 1 3 4c0-.6.4-1 1-1h3.5c.6 0 1 .4 1 1 0 1.3.2 2.5.6 3.6.1.3 0 .7-.2 1z"/></svg>
        561-730-2254
      </li>
      <li>
        <svg viewBox="0 0 24 24"><path d="M6 2h12v5H6zM4 8h16a2 2 0 0 1 2 2v7h-4v5H6v-5H2v-7a2 2 0 0 1 2-2zm4 8v4h8v-4z"/></svg>
        561-730-2255
      </li>
      <li>
        <svg viewBox="0 0 24 24"><path d="M2 5h20v14H2zm2 2v.5l8 5 8-5V7z"/></svg>
        laura@maplecrestcc-example.com
      </li>
      <li>
        <svg viewBox="0 0 24 24"><path d="M12 2a7 7 0 0 0-7 7c0 5 7 13 7 13s7-8 7-13a7 7 0 0 0-7-7zm0 9.5A2.5 2.5 0 1 1 12 6.5a2.5 2.5 0 0 1 0 5z"/></svg>
        4382 W. Harbor Parkway, Suite 714 Boca Raton, FL 33912
      </li>
    </ul>

    <div class="website">www.maplecrestcc-example.com</div>
  </div>
</body>
</html>
```